Byte Wardens Inc. IT Services and Sales

We need a new business card design for our new company. We have a current logo but are open and encourage any redesigns.

Byte Wardens is derived in our history from computer gaming. (NovaFront References, SURGE UNLEASHED!!!). We as a group have been together since high school (2002). Our friendships brought us together and now we are all business partners providing IT Support and Consultation Services ranging from fixing small issues like printers, home networking, pc building to custom application development and managed cloud and it networks for our clients.
We would like our design to communicate that we strive to be the best (we are born gamers and have a highly competitive instinct) and offer solutions to problems that other companies just simply say we can't do it. We are always looking to go above and beyond for our clients, learning our clients business and figuring out ways to help them make more money by optimizing the way they do business, offering solutions so they can grow their business and helping everyone utilize the technology they have or advise them with the technology they need to succeed.

Attached are things we have on our computers and logo's we have used.
One is a desktop background
while the other should be our logo.

Again, we are open to and encourage any logo redesigns in hope things can help with the direction we are looking into.

Please add a place for email as our current cards have no email and it makes us very sad.
Updates

Hi All,

Just wanted to say thank you for all those who submitted a design. We've updated our project to include the fact that we are open and encourage a logo redesign. Also, this project is now committed to payment.

Target Market(s)

We will be handing these out to all our future business prospects. Prospects are usually business owners that can be in any industry. They look to us to be cutting edge or professional.

Industry/Entity Type

High School

Requirements
Must have
• name, title, work, fax, and cell phone, address and email

```html
<!DOCTYPE html>
<html lang="en">
<head>
<meta charset="utf-8">
<title>Byte Wardens Business Card</title>
<link rel="stylesheet" href="https://fonts.googleapis.com/css2?family=Open+Sans:wght@400;600;700&display=swap">
<style>
  :root {
    --page: #d9d9d9;
    --card: #38383a;
    --silver: #e6e6e6;
    --muted: #c9c9c9;
    --accent: #e35f2b;
  }
  * { box-sizing: border-box; margin: 0; padding: 0; }
  html, body { width: 1200px; height: 1000px; overflow: hidden; }
  body {
    background: var(--page);
    font-family: "Open Sans", sans-serif;
    position: relative;
  }
  .card {
    position: absolute;
    left: 200px;
    width: 800px;
    height: 457px;
    background: var(--card);
    border-radius: 26px;
    color: var(--silver);
  }
  .card--front { top: 30px; }
  .card--back { top: 513px; }

  .front-brand {
    position: absolute;
    left: 0; right: 0; top: 160px;
    text-align: center;
  }
  .wordmark {
    display: inline-flex;
    align-items: center;
    gap: 18px;
    font-weight: 700;
    font-size: 64px;
    letter-spacing: 4px;
    color: var(--silver);
    text-transform: uppercase;
  }
  .wordmark__square {
    width: 40px; height: 40px;
    background: var(--accent);
  }
  .tagline {
    margin-top: 10px;
    font-weight: 600;
    font-size: 20px;
    letter-spacing: 3px;
    color: var(--silver);
  }

  .back-brand {
    position: absolute;
    left: 60px; top: 200px;
  }
  .back-brand .wordmark { font-size: 40px; letter-spacing: 3px; gap: 14px; }
  .back-brand .wordmark__square { width: 26px; height: 26px; }

  .contact {
    position: absolute;
    left: 480px; top: 70px;
  }
  .contact__name {
    font-weight: 600;
    font-size: 26px;
    color: var(--accent);
    letter-spacing: 1px;
  }
  .contact__title {
    font-size: 19px;
    color: var(--muted);
    margin-top: -2px;
  }
  .contact__list {
    list-style: none;
    margin-top: 54px;
  }
  .contact__item {
    display: flex;
    align-items: center;
    gap: 12px;
    font-size: 20px;
    color: var(--silver);
    height: 34px;
  }
  .contact__icon { width: 20px; height: 20px; fill: var(--accent); flex: none; }
  .address {
    position: absolute;
    left: 480px; top: 350px;
    font-size: 20px;
    line-height: 1.3;
    color: var(--muted);
  }
</style>
</head>
<body>
  <section class="card card--front">
    <div class="front-brand">
      <div class="wordmark"><span class="wordmark__square"></span>Byte Wardens</div>
      <p class="tagline">RETAIL | IT SERVICES | IT CONSULTATION | MARKETING</p>
    </div>
  </section>

  <section class="card card--back">
    <div class="back-brand">
      <div class="wordmark"><span class="wordmark__square"></span>Byte Wardens</div>
    </div>

    <div class="contact">
      <p class="contact__name">MARCUS HALE</p>
      <p class="contact__title">Director of Operations</p>
      <ul class="contact__list">
        <li class="contact__item">
          <svg class="contact__icon" viewBox="0 0 20 20" aria-hidden="true"><rect x="5" y="1" width="10" height="18" rx="2"/><rect x="7" y="4" width="6" height="8" fill="#38383a"/></svg>
          (555) 214 7730
        </li>
        <li class="contact__item">
          <svg class="contact__icon" viewBox="0 0 20 20" aria-hidden="true"><path d="M4 2l4 1 1 4-2 2a11 11 0 0 0 4 4l2-2 4 1 1 4-2 2C9 18 2 11 2 4z"/></svg>
          (555) 482 1096
        </li>
        <li class="contact__item">
          <svg class="contact__icon" viewBox="0 0 20 20" aria-hidden="true"><rect x="5" y="1" width="10" height="6"/><rect x="2" y="8" width="16" height="8" rx="1"/><rect x="5" y="13" width="10" height="6" fill="#e35f2b" stroke="#38383a" stroke-width="1"/></svg>
          (555) 609 3385
        </li>
        <li class="contact__item">
          <svg class="contact__icon" viewBox="0 0 20 20" aria-hidden="true"><rect x="1" y="4" width="18" height="12"/><path d="M1 4l9 7 9-7" fill="none" stroke="#38383a" stroke-width="1.5"/></svg>
          yourname@bytewardens.com
        </li>
      </ul>
    </div>

    <p class="address">4470 Calloway Ave.,<br>Suite B, Westbrook, CA. 90210</p>
  </section>
</body>
</html>
```